Flyer Tally Your Ledger Free

Hi
Can you please design me a DL Flyer for: Tally Your Ledger Free
Info:
Starting a new Business ?
Want to save on bookkeeping fees for your existing business?

You can now save 1000's off bookkeeping fees by Doing it Yourself.

Using our Bookkeeper software you simply key in the information as you go.

We offer one on one training, backup and support.
We can assist you with BAS Preparation and Payrol Advice.

Add Modules as required:
Point of Sale Module
Jobs Management Module
Website Intergration Module

Fee set up assistance and training.

Lets get the ball rolling: 1300 642 815
www.tylfr.com.au
admin@tylfr.com.au (use the logo thing you made)

Target Market(s)

Small Business

Colors
ec1f27
f04a50
f59296
fcdcdc
ffffff

Requirements
Nice to have
• image/s related to bookkeeping

```html
<!DOCTYPE html>
<html lang="en">
<head>
<meta charset="utf-8">
<title>Tally Your Ledger Free – DL Flyer Options</title>
<link rel="stylesheet" href="https://fonts.googleapis.com/css2?family=Fira+Sans:wght@400;500;600;700&display=swap">
<style>
  :root {
    --red: #ec1f27;
    --red-soft: #f04a50;
    --pink: #f59296;
    --blush: #fcdcdc;
    --white: #ffffff;
    --board: #ececec;
    --panel: #6b6c6f;
    --fold: #48494c;
    --highlight: #58595b;
    --ink: #3d3e40;
    --muted: #6d6e71;
    --caption: #9a9a9a;
    --gold: #f2b632;
  }
  * { box-sizing: border-box; margin: 0; padding: 0; }
  html, body { width: 1200px; height: 1200px; overflow: hidden; }
  body {
    background: var(--board);
    font-family: "Fira Sans", Arial, sans-serif;
    position: relative;
  }
  .flyer {
    position: absolute;
    top: 216px;
    width: 455px;
    height: 910px;
    background: var(--white);
    transform: scale(0.8);
    transform-origin: top left;
    overflow: hidden;
  }
  .flyer--variant { left: 222px; }
  .flyer--standard { left: 658px; }
  .flyer__bg { position: absolute; inset: 0; }
  .abs { position: absolute; }

  .brand { left: 25px; top: 38px; display: flex; align-items: center; gap: 8px; }
  .brand__dot { width: 22px; height: 22px; border-radius: 50%; background: var(--red); }
  .brand__name { font-size: 25px; font-weight: 500; color: var(--red); letter-spacing: -0.3px; }

  .icon-ph { border-radius: 6px; }

  .intro { font-size: 24px; line-height: 25px; color: var(--muted); }
  .intro strong { font-weight: 600; color: var(--ink); }
  .flyer--variant .intro { left: 25px; top: 137px; }
  .flyer--standard .intro { left: 112px; top: 137px; color: var(--white); font-weight: 600; font-size: 32px; line-height: 37px; }
  .flyer--standard .intro strong { color: var(--white); }

  .headline { left: 212px; top: 222px; font-size: 30px; font-weight: 700; line-height: 32px; color: var(--white); }
  .headline span { display: inline-block; background: var(--highlight); padding: 0 4px 0 3px; margin-bottom: 0; }

  .saving { left: 213px; top: 457px; font-size: 20px; font-weight: 600; line-height: 22.5px; color: var(--white); }

  .software { left: 42px; top: 374px; font-size: 24px; line-height: 27.4px; color: var(--white); }
  .software .small { font-size: 19px; }

  .contact { left: 20px; top: 738px; color: var(--ink); }
  .contact__lead { font-size: 13px; font-weight: 500; }
  .contact__phone { display: inline-block; margin-top: 6px; background: var(--red); color: var(--white); font-size: 20px; font-weight: 500; padding: 0 7px; line-height: 25px; letter-spacing: 0.4px; }
  .contact__web { font-size: 16px; margin-top: 5px; color: var(--muted); }
  .contact__mail { font-size: 14px; margin-top: 6px; color: var(--muted); }

  .divider { left: 181px; top: 600px; width: 2px; height: 310px; background: #9d9ea1; }

  .points { left: 190px; top: 607px; width: 255px; list-style: none; }
  .points li { position: relative; padding-left: 23px; font-size: 14px; line-height: 17px; color: var(--muted); margin-bottom: 9px; }
  .points li strong { color: var(--ink); font-weight: 600; }
  .points svg { position: absolute; left: 0; top: 3px; }

  .modules { left: 213px; top: 710px; list-style: none; }
  .modules li { display: flex; align-items: center; gap: 20px; height: 55px; margin-bottom: 10px; }
  .modules .icon-ph { width: 53px; height: 53px; background: #d7d8da; }
  .modules span { font-size: 15px; line-height: 17px; font-weight: 500; color: var(--ink); }

  .caption { position: absolute; top: 969px; width: 364px; text-align: center; font-size: 21px; color: var(--caption); }
</style>
</head>
<body>

<!-- Option 01 -->
<section class="flyer flyer--variant">
  <svg class="flyer__bg" viewBox="0 0 455 910" width="455" height="910" aria-hidden="true">
    <path d="M362 0H455V500C380 570 280 595 182 600V300L107 212C230 198 330 120 362 0Z" fill="var(--red)"/>
    <path d="M107 212L182 300L107 312Z" fill="var(--fold)"/>
    <path d="M0 322L182 300V690C110 692 50 700 0 720Z" fill="var(--panel)"/>
  </svg>

  <div class="abs brand"><span class="brand__dot"></span><span class="brand__name">Tally Your Ledger Free</span></div>
  <div class="abs icon-ph" role="img" aria-label="Briefcase icon" style="left:25px;top:103px;width:38px;height:30px;background:var(--gold);"></div>
  <p class="abs intro">Starting<br><strong>a new Business?</strong></p>

  <div class="abs icon-ph" role="img" aria-label="Light bulb icon" style="left:172px;top:222px;width:32px;height:46px;background:var(--gold);border-radius:16px 16px 6px 6px;"></div>
  <p class="abs headline"><span>WANT TO</span><br><span>SAVE ON</span><br><span>BOOKKEEPING</span><br><span>FEES FOR</span><br><span>YOUR</span><br><span>EXISTING</span><br><span>BUSINESS?</span></p>

  <div class="abs icon-ph" role="img" aria-label="Piggy bank icon" style="left:172px;top:452px;width:36px;height:28px;background:var(--blush);border-radius:14px;"></div>
  <p class="abs saving">You can now save<br>1000’s off bookkeeping<br>fees by Doing it<br>Yourself.</p>

  <div class="abs icon-ph" role="img" aria-label="Growth chart icon" style="left:75px;top:322px;width:46px;height:48px;background:var(--red);"></div>
  <p class="abs software">Using our<br><span class="small">Bookkeeper</span><br>software<br>you simply<br>key in the<br>information<br>as you go.</p>

  <div class="abs" role="img" aria-label="Rocket illustration" style="left:38px;top:582px;width:110px;height:108px;background:linear-gradient(135deg,var(--gold),#e9962a);border-radius:60% 10% 60% 10%;"></div>

  <div class="abs contact">
    <p class="contact__lead">Lets get the ball rolling:</p>
    <p class="contact__phone">1300 642 815</p>
    <p class="contact__web">www.tylfr.com.au</p>
    <p class="contact__mail">admin@tylfr.com.au</p>
  </div>
  <div class="abs icon-ph" role="img" aria-label="Pointing hand icon" style="left:72px;top:842px;width:36px;height:52px;background:#d7d8da;"></div>

  <div class="abs divider"></div>
  <ul class="abs points">
    <li><svg width="13" height="13" viewBox="0 0 13 13"><path d="M1 1L12 6.5L1 12Z" fill="none" stroke="var(--red)" stroke-width="1.6"/></svg>We offer one on one <strong>training, backup and support.</strong></li>
    <li><svg width="13" height="13" viewBox="0 0 13 13"><path d="M1 1L12 6.5L1 12Z" fill="none" stroke="var(--red)" stroke-width="1.6"/></svg>We can assist you with <strong>BAS</strong> Preparation and <strong>Payrol</strong> Advice.</li>
  </ul>
  <ul class="abs modules">
    <li><div class="icon-ph" role="img" aria-label="Point of sale register icon"></div><span>Point of Sale<br>Module</span></li>
    <li><div class="icon-ph" role="img" aria-label="Team management icon"></div><span>Jobs Management<br>Module</span></li>
    <li><div class="icon-ph" role="img" aria-label="Website browser icon"></div><span>Website Intergration<br>Module</span></li>
  </ul>
</section>
<p class="caption" style="left:222px;">Option 01, Color Varions</p>

<!-- Option 02 -->
<section class="flyer flyer--standard">
  <svg class="flyer__bg" viewBox="0 0 455 910" width="455" height="910" aria-hidden="true">
    <path d="M0 160C150 140 300 80 382 0H455V500C380 570 280 595 182 600V300L0 178Z" fill="var(--red)"/>
    <path d="M0 178L182 300L0 322Z" fill="var(--fold)"/>
    <path d="M0 322L182 300V690C110 692 50 700 0 720Z" fill="var(--panel)"/>
  </svg>

  <div class="abs brand"><span class="brand__dot"></span><span class="brand__name">Tally Your Ledger Free</span></div>
  <p class="abs intro">Starting<br><strong>a new Business?</strong></p>
  <div class="abs icon-ph" role="img" aria-label="Briefcase icon" style="left:246px;top:143px;width:38px;height:30px;background:var(--blush);"></div>

  <div class="abs icon-ph" role="img" aria-label="Light bulb icon" style="left:172px;top:222px;width:32px;height:46px;background:var(--white);border-radius:16px 16px 6px 6px;"></div>
  <p class="abs headline"><span>WANT TO</span><br><span>SAVE ON</span><br><span>BOOKKEEPING</span><br><span>FEES FOR</span><br><span>YOUR</span><br><span>EXISTING</span><br><span>BUSINESS?</span></p>

  <div class="abs icon-ph" role="img" aria-label="Piggy bank icon" style="left:172px;top:452px;width:36px;height:28px;background:var(--blush);border-radius:14px;"></div>
  <p class="abs saving">You can now save<br>1000’s off bookkeeping<br>fees by Doing it<br>Yourself.</p>

  <div class="abs icon-ph" role="img" aria-label="Growth chart icon" style="left:75px;top:322px;width:46px;height:48px;background:var(--red);"></div>
  <p class="abs software">Using our<br><span class="small">Bookkeeper</span><br>software<br>you simply<br>key in the<br>information<br>as you go.</p>

  <div class="abs" role="img" aria-label="Rocket illustration" style="left:38px;top:582px;width:110px;height:108px;background:linear-gradient(135deg,var(--red-soft),var(--red));border-radius:60% 10% 60% 10%;"></div>

  <div class="abs contact">
    <p class="contact__lead">Lets get the ball rolling:</p>
    <p class="contact__phone">1300 642 815</p>
    <p class="contact__web">www.tylfr.com.au</p>
    <p class="contact__mail">admin@tylfr.com.au</p>
  </div>
  <div class="abs icon-ph" role="img" aria-label="Pointing hand icon" style="left:72px;top:842px;width:36px;height:52px;background:#d7d8da;"></div>

  <div class="abs divider"></div>
  <ul class="abs points">
    <li><svg width="13" height="13" viewBox="0 0 13 13"><path d="M1 1L12 6.5L1 12Z" fill="none" stroke="var(--red)" stroke-width="1.6"/></svg>We offer one on one <strong>training, backup and support.</strong></li>
    <li><svg width="13" height="13" viewBox="0 0 13 13"><path d="M1 1L12 6.5L1 12Z" fill="none" stroke="var(--red)" stroke-width="1.6"/></svg>We can assist you with <strong>BAS</strong> Preparation and <strong>Payrol</strong> Advice.</li>
  </ul>
  <ul class="abs modules">
    <li><div class="icon-ph" role="img" aria-label="Point of sale register icon"></div><span>Point of Sale<br>Module</span></li>
    <li><div class="icon-ph" role="img" aria-label="Team management icon"></div><span>Jobs Management<br>Module</span></li>
    <li><div class="icon-ph" role="img" aria-label="Website browser icon"></div><span>Website Intergration<br>Module</span></li>
  </ul>
</section>
<p class="caption" style="left:658px;">Option 02, standerd colors</p>

</body>
</html>
```